Real Estate Newsletter

I would like a template created for a monthly newsletter; ideally, two pages long, including my photo, logo and contact info. I need it to look professional and be very easy for me to drop text into.

Target Market(s)

Past/current clients

Industry/Entity Type

Real Estate Agent

Font styles to use
Serif

Requirements
Must have
• My contact info/photo and logo
• (206) 555-0187
• mkettridge@lunvoro.com
• www.MarlaKettridge.com
Nice to have
• I need a template where I can easily drop contact. I need the template to look professional so I can print it and mail it to current and past clients.

```html
<!DOCTYPE html>
<html lang="en">
<head>
<meta charset="utf-8">
<title>Marla Kettridge – Client Newsletter</title>
<link rel="stylesheet" href="https://fonts.googleapis.com/css2?family=Libre+Baskerville:wght@400;700&display=swap">
<style>
  :root {
    --backdrop: #d5d6da;
    --page: #ffffff;
    --lavender: #c8cbe6;
    --navy: #1f2456;
    --brand-blue: #2e3a9a;
    --ring: #9aa0d4;
    --ink: #1a1a1a;
    --photo-tone: #b9a48f;
  }
  * { box-sizing: border-box; margin: 0; padding: 0; }
  html, body { width: 1200px; height: 1200px; overflow: hidden; background: #fff; }
  .canvas { position: relative; width: 1200px; height: 1200px; background: #fff; }
  .backdrop { position: absolute; left: 56px; top: 50px; width: 1102px; height: 1102px; background: var(--backdrop); }
  .page { position: absolute; left: 82px; top: 76px; width: 1056px; height: 1054px; background: var(--page); }

  .masthead { position: absolute; left: 86px; top: 0; width: 510px; height: 232px; }
  .masthead svg { position: absolute; left: 0; top: 0; }
  .brand-name {
    position: absolute; left: 0; top: 96px; width: 510px; text-align: center;
    font-family: "Libre Baskerville", serif; font-weight: 700; font-size: 40px;
    color: var(--brand-blue); letter-spacing: -0.5px;
  }

  .section-bar {
    position: absolute; left: 86px; top: 254px; width: 510px; height: 44px;
    background: var(--lavender); display: flex; align-items: center; justify-content: center;
    font-family: "Libre Baskerville", serif; font-size: 21px; letter-spacing: 1px; color: var(--brand-blue);
  }

  .reviews {
    position: absolute; left: 86px; top: 313px; width: 510px; height: 660px; overflow: hidden;
    font-family: "Libre Baskerville", serif; font-size: 15px; line-height: 19.6px;
    letter-spacing: 1.7px; color: var(--ink); text-align: justify;
  }
  .review { text-indent: 26px; margin-bottom: 19.6px; }

  .page-marker {
    position: absolute; left: 86px; top: 1016px; width: 510px;
    font-family: "Libre Baskerville", serif; font-size: 12px; letter-spacing: 1px; color: var(--brand-blue);
  }

  .column-rule { position: absolute; left: 677px; top: 226px; width: 0; height: 766px; border-left: 2px dashed var(--brand-blue); }

  .portrait {
    position: absolute; left: 754px; top: 36px; width: 232px; height: 232px; border-radius: 50%;
    border: 6px solid var(--ring);
    background: radial-gradient(circle at 50% 40%, #e6d9cc 0%, var(--photo-tone) 55%, #f3f2f2 100%);
  }

  .about-rule { position: absolute; left: 754px; width: 252px; border-top: 2px dashed var(--brand-blue); }
  .about-rule.top { top: 290px; }
  .about-rule.bottom { top: 350px; }
  .about-title {
    position: absolute; left: 754px; top: 304px; width: 252px; text-align: center;
    font-family: "Libre Baskerville", serif; font-weight: 400; font-size: 19px; letter-spacing: 3px; color: var(--brand-blue);
  }
  .about-text {
    position: absolute; left: 768px; top: 370px; width: 222px; text-align: center;
    font-family: "Libre Baskerville", serif; font-size: 13.6px; line-height: 17.9px;
    letter-spacing: 1.4px; color: var(--brand-blue);
  }

  .contact {
    position: absolute; left: 740px; top: 990px; width: 280px; text-align: center; list-style: none;
    font-family: "Libre Baskerville", serif; font-size: 11.5px; line-height: 16px;
    letter-spacing: 0.5px; color: var(--brand-blue);
  }
</style>
</head>
<body>
<div class="canvas">
  <div class="backdrop"></div>
  <div class="page">
    <header class="masthead">
      <svg width="510" height="232" viewBox="0 0 510 232" aria-hidden="true">
        <polygon points="0,0 510,0 510,190 254,230 0,190" fill="var(--lavender)"/>
        <polyline points="10,194 254,230 500,194" fill="none" stroke="var(--navy)" stroke-width="4"/>
      </svg>
      <div class="brand-name">MarlaKettridge</div>
    </header>

    <div class="section-bar">Client Review</div>

    <section class="reviews">
      <p class="review">Marla is amazing! She helped us get top dollar for our old home, and to make a competitive offer on our new one that secured us the house of our dreams. We must have toured through 15-20 different houses looking for our dream home. She was so insightful and helpful as we tried to decide, as my husband and I had some different must-haves. Once we decided on the house for us, she crafted a strategy that enabled us to beat the competition without throwing all our money on the table. I felt we got our house for a fair price - and she was right on the money when it came to her predicted final sale price. She helped us clean, stage and sell our old home and get a quick close that met our sales goal. Her great sales skills helped ensure we received several good offers to choose from. I LOVE our new house and hope we never have to move again - but if we do, I know who I’ll call. I can’t recommend her highly enough, and am always referring family and friends her way. Thanks so much Marla! &nbsp;&nbsp;&nbsp;&nbsp; - Corinne &amp; Theo Valdmarsh, Shoreline</p>
      <p class="review">We were looking for a single family home in the Lake Forest Park area and we wanted an agent who knew the neighborhood and could guide us through our first home purchase. We are glad we chose Marla. She is honest and has a go-getter personality that is necessary in this competitive market. She was never pushy, gave us the best advice on making our offer competitive and we could not be more happy with her. We have no hesitation referring her to family and friends! &nbsp;&nbsp;&nbsp;&nbsp; - Anish &amp; Leela Varadan, Lake Forest Park</p>
    </section>

    <div class="page-marker">Page 1 of 2</div>

    <div class="column-rule"></div>

    <div class="portrait" role="img" aria-label="Portrait photo of Marla Kettridge"></div>
    <div class="about-rule top"></div>
    <h2 class="about-title">ABOUT</h2>
    <div class="about-rule bottom"></div>
    <p class="about-text">I have spent my entire life in the Seattle area. I was born and raised in Greenlake- before Ballard and Greenlake were "cool" areas- back when they were still small, sleepy Seattle neighborhoods. It was my husband who first introduced me to real estate. His father had made a living purchasing homes, rehabbing them and turning them into long term rental properties. At his encouragement, we purchased our first home- a run down shack literally encroaching on an off ramp of I5. I couldn't see the vision, but blindly followed. Fast forward 7+ years and we own a handful of rental properties throughout Seattle, Shoreline and Lake Forest Park that we've rehabbed and manage ourselves.</p>

    <ul class="contact">
      <li>(206) 555-0187</li>
      <li>mkettridge@lunvoro.com</li>
      <li>www.MarlaKettridge.com</li>
    </ul>
  </div>
</div>
</body>
</html>
```